Carpet cleaning company wants business card

Need an exciting new fresh design for business cards for my carpet cleaning /pest control business
www.tidewellhomecare.com.au
Can design include a lined section for quoting or information? Thanks !

```html
<!DOCTYPE html>
<html lang="en">
<head>
<meta charset="utf-8">
<title>Tidewell Home Care – Business Card</title>
<link rel="stylesheet" href="https://fonts.googleapis.com/css2?family=Montserrat:wght@400;500;700;800&display=swap">
<style>
  :root {
    --brand-red: #e8413a;
    --brand-blue: #0b56a8;
    --frame-orange: #ee5a2a;
    --ink: #2a2a2a;
    --rule: #b9c6d8;
    --card: #ffffff;
    --backdrop: #e9e7e4;
  }
  * { box-sizing: border-box; margin: 0; padding: 0; }
  html, body {
    width: 1200px; height: 900px; overflow: hidden;
    background: var(--backdrop);
    font-family: "Montserrat", Arial, sans-serif;
    color: var(--ink);
  }
  .sheet {
    position: relative; width: 1200px; height: 900px;
    display: flex; flex-direction: column; align-items: center; justify-content: center; gap: 40px;
  }
  .card {
    position: relative; width: 700px; height: 400px;
    background: var(--card); border-radius: 36px;
    box-shadow: 0 6px 18px rgba(0,0,0,.12);
    overflow: hidden;
  }
  .card__frame { position: absolute; inset: 20px; border-radius: 26px; }
  .card--back .card__frame { border: 1.5px solid var(--brand-blue); }
  .card--front .card__frame { border: 2px solid var(--frame-orange); }

  .wordmark {
    font-weight: 800; color: var(--brand-blue);
    letter-spacing: .01em; text-transform: uppercase; line-height: 1;
    display: flex; align-items: center; gap: 14px; white-space: nowrap;
  }
  .wordmark__mark { width: 18px; height: 18px; background: var(--brand-red); flex: none; }

  .services {
    font-size: 14px; font-weight: 700; letter-spacing: .32em;
    text-transform: uppercase; color: #fff; background: var(--brand-blue);
    padding: 5px 12px; white-space: nowrap; display: inline-block;
  }

  /* Back: brand + lined quote section */
  .card--back .wordmark { position: absolute; left: 50px; top: 52px; font-size: 38px; }
  .card--back .wordmark__mark { width: 26px; height: 26px; }
  .card--back .services { position: absolute; left: 50px; top: 104px; }

  .quote { position: absolute; left: 50px; right: 50px; top: 152px; }
  .quote__title {
    font-size: 14px; font-weight: 700; color: var(--brand-red);
    text-transform: uppercase; letter-spacing: .12em; margin-bottom: 4px;
  }
  .quote__row {
    display: flex; align-items: flex-end; gap: 12px;
    height: 38px; border-bottom: 1.5px solid var(--rule);
    font-size: 14px; font-weight: 500; color: var(--brand-blue); padding-bottom: 4px;
  }
  .quote__row span { width: 74px; flex: none; }

  /* Front */
  .card--front .wordmark { position: absolute; left: 44px; top: 42px; font-size: 30px; }
  .card--front .services { position: absolute; left: 44px; top: 82px; font-size: 12px; letter-spacing: .3em; }

  .person { position: absolute; right: 48px; top: 150px; text-align: right; }
  .person__name { font-weight: 700; font-size: 26px; letter-spacing: .04em; }
  .person__first { color: var(--brand-red); }
  .person__last { color: var(--brand-blue); }
  .person__role { font-size: 19px; font-weight: 500; margin-top: 6px; letter-spacing: .02em; }

  .side-tab {
    position: absolute; right: 0; top: 170px; width: 14px; height: 64px;
    background: var(--brand-blue);
  }

  .contacts { position: absolute; left: 40px; bottom: 40px; list-style: none; }
  .contacts li {
    display: flex; align-items: center; gap: 10px;
    font-size: 17px; font-weight: 500; line-height: 1.55;
  }
  .contacts svg { width: 16px; height: 16px; flex: none; fill: var(--brand-red); }

  .address {
    position: absolute; right: 54px; bottom: 44px;
    font-size: 17px; font-weight: 500; line-height: 1.55; font-style: normal;
  }
</style>
</head>
<body>
<main class="sheet">
  <section class="card card--back" aria-label="Card back">
    <div class="card__frame"></div>
    <div class="wordmark"><span class="wordmark__mark"></span>Tidewell Home Care</div>
    <p class="services">Carpet Cleaning · Pest Control</p>
    <div class="quote">
      <p class="quote__title">Quote / Notes</p>
      <div class="quote__row"><span>Date</span></div>
      <div class="quote__row"><span>Service</span></div>
      <div class="quote__row"><span>Price</span></div>
      <div class="quote__row"><span>Notes</span></div>
    </div>
  </section>

  <section class="card card--front" aria-label="Card front">
    <div class="card__frame"></div>
    <div class="wordmark"><span class="wordmark__mark"></span>Tidewell Home Care</div>
    <p class="services">Carpet Cleaning · Pest Control</p>

    <div class="person">
      <p class="person__name"><span class="person__first">LIAM</span> <span class="person__last">PORTER</span></p>
      <p class="person__role">Managing Director</p>
    </div>
    <div class="side-tab"></div>

    <ul class="contacts">
      <li>
        <svg viewBox="0 0 24 24" aria-hidden="true"><path d="M6.6 10.8a15 15 0 0 0 6.6 6.6l2.2-2.2a1 1 0 0 1 1-.25 11.4 11.4 0 0 0 3.6.57 1 1 0 0 1 1 1V20a1 1 0 0 1-1 1A17 17 0 0 1 3 4a1 1 0 0 1 1-1h3.5a1 1 0 0 1 1 1c0 1.250.2 2.450.57 3.57a1 1 0 0 1-.25 1z"/></svg>
        07 5550 2184
      </li>
      <li>
        <svg viewBox="0 0 24 24" aria-hidden="true"><path d="M7 1h10a2 2 0 0 1 2 2v18a2 2 0 0 1-2 2H7a2 2 0 0 1-2-2V3a2 2 0 0 1 2-2zm0 3v14h10V4zm5 15.5a1.2 1.2 0 1 0 0 2.4 1.2 1.2 0 0 0 0-2.4z"/></svg>
        0400 555 926
      </li>
      <li>
        <svg viewBox="0 0 24 24" aria-hidden="true"><path d="M2 5h20v14H2zm2 2v.5l8 5 8-5V7zm0 2.8V17h16V9.8l-8 5z"/></svg>
        admin@tidewellhomecare.com.au
      </li>
      <li>
        <svg viewBox="0 0 24 24" aria-hidden="true"><path d="M12 2a10 10 0 1 0 0 20 10 10 0 0 0 0-20zm0 2c.8 1.2 1.5 2.5 1.9 4h-3.8c.4-1.5 1.1-2.8 1.9-4zM4.3 14a8 8 0 0 1 0-4h3.4a16 16 0 0 0 0 4zm5.4 0a14 14 0 0 1 0-4h4.6a14 14 0 0 1 0 4zm6.6 0a16 16 0 0 0 0-4h3.4a8 8 0 0 1 0 4zM12 20c-.8-1.2-1.5-2.5-1.9-4h3.8c-.4 1.5-1.1 2.8-1.9 4z"/></svg>
        www.tidewellhomecare.com.au
      </li>
    </ul>

    <address class="address">Your address, City<br>State, Zip 1234</address>
  </section>
</main>
</body>
</html>
```